We are an Estate agency (Real estate)– looking for Christmas/winter theme leaflet

We are called ‘’HOLLIVERS’’ we are an estate agency based in England. We opened in 2020 in February, few weeks before Covid and we are now known as one of the fastest growing agencies in all of Brighton and Hove.
This is our first Christmas/winter leaflet and this kind of offer!
Offer is: if the client signs with us to sell their home from 1st December 2021 until 7th January 2022 they will receive 50% off HOLLIVERS fees.
I am looking for A5 two-sided leaflet. The first side should contain our branding, the offer. Also, maybe this: ‘’ Let us Treat you this Christmas’’ or maybe on the other side of leaflet, which will contain explanation of the offer, our office details etc. the back should also contain some design.
Our target market is higher end clients who own a property in Brighton and Hove and looking to sell. I would say target market 35+ years of age.
Our branding is clean, fresh and eye catching and that’s what leaflet should look like and represent.
I will insert our website link so you could have a look at the properties that we deal with too. I could also insert last leaflet which I designed and had a really positive response & feedback… maybe will give you some ideas.
I have inserted our brand guidelines. We use Hollivers in white or blue backgrounds as in guideline.
https://www.holliversestateagents.co.uk/
Hi guys,
Thank you for all your ideas so far, however just wanted to mention that I am looking for not so much ''in your face Christmas'' design - something subtle.
Needs to be classy, modern and eye catching - our target market is property owners 35+ years of age. Moreover, this offer needs to be perceived as one off opportunity.
35+ property owners

```html
<!DOCTYPE html>
<html lang="en">
<head>
<meta charset="utf-8">
<title>Hollivers – Christmas Leaflet</title>
<link rel="stylesheet" href="https://fonts.googleapis.com/css2?family=Ubuntu:wght@300;400;500;700&display=swap">
<style>
  :root {
    --stage: #0b0b0b;
    --paper: #ffffff;
    --brand-red: #c00000;
    --deep-red: #a80000;
    --edge-red: #7a0000;
    --ink: #1e1e1e;
    --white: #ffffff;
  }
  * { box-sizing: border-box; margin: 0; padding: 0; }
  html, body { width: 1200px; height: 900px; overflow: hidden; background: var(--stage); }
  body { position: relative; font-family: "Ubuntu", sans-serif; color: var(--ink); }

  .leaflet { position: absolute; top: 146px; width: 444px; height: 630px; overflow: hidden; }
  .leaflet--back { left: 159px; background: var(--paper); }
  .leaflet--front {
    left: 614px;
    background: linear-gradient(90deg, var(--edge-red) 0%, var(--deep-red) 25%, #b50000 50%, var(--deep-red) 75%, var(--edge-red) 100%);
  }

  /* brand name */
  .brand-name { position: absolute; font-weight: 700; white-space: nowrap; text-align: center; }
  .leaflet--back .brand-name {
    left: 14px; top: 79px; width: 104px;
    font-size: 13px; letter-spacing: 2.4px; color: var(--brand-red);
  }
  .leaflet--front .brand-name {
    left: 0; top: 182px; width: 444px;
    font-size: 25px; letter-spacing: 4.5px; color: var(--white);
  }

  /* photo column */
  .accent-bar { position: absolute; left: 0; top: 115px; width: 41px; height: 328px; background: var(--deep-red); }
  .gallery { position: absolute; left: 49px; top: 115px; width: 123px; height: 328px; display: flex; flex-direction: column; gap: 1px; }
  .gallery__photo { flex: 1; }
  .gallery__photo--1 { background: linear-gradient(180deg, #6f9ccf 0%, #e8eef2 45%, #c9cdc8 75%, #7b7d78 100%); }
  .gallery__photo--2 { background: linear-gradient(180deg, #a3462f 0%, #e6e3de 45%, #f0efec 65%, #8c5a4a 100%); }
  .gallery__photo--3 { background: linear-gradient(180deg, #6f9ad2 0%, #b6633f 45%, #7f8b52 75%, #9a7d66 100%); }
  .gallery__photo--4 { background: linear-gradient(180deg, #9ab1c4 0%, #b35a3b 40%, #59743d 75%, #a9794f 100%); }

  /* office details */
  .office-icon { position: absolute; left: 20px; top: 454px; width: 27px; height: 27px; }
  .details { position: absolute; left: 19px; font-size: 10.5px; line-height: 17px; color: var(--ink); }
  .details__title { font-size: 12px; font-weight: 500; line-height: 14px; }
  .details--office { top: 485px; }
  .details--hours { top: 533px; }

  /* headline */
  .headline {
    position: absolute; right: 17px; top: 22px;
    text-align: right; color: var(--brand-red);
    font-size: 74px; font-weight: 700; line-height: 62px; letter-spacing: -1.5px;
  }
  .offer {
    position: absolute; right: 17px; top: 214px;
    text-align: right; font-size: 15.5px; font-weight: 400; line-height: 21.5px; color: var(--ink);
    white-space: nowrap;
  }

  /* story */
  .story-rule { position: absolute; left: 204px; top: 303px; width: 3px; height: 306px; background: var(--brand-red); }
  .story { position: absolute; left: 224px; top: 300px; width: 203px; }
  .story__title { font-size: 14.5px; font-weight: 500; color: var(--brand-red); white-space: nowrap; line-height: 18px; }
  .story__body { margin-top: 0; font-size: 11.9px; font-weight: 400; line-height: 18px; text-align: justify; color: var(--ink); }

  /* contact */
  .contact-icons { position: absolute; left: 222px; top: 561px; width: 18px; display: flex; flex-direction: column; gap: 3px; }
  .contact-icons svg { width: 16px; height: 13px; display: block; }
  .contact {
    position: absolute; left: 246px; top: 557px; width: 198px; height: 52px;
    background: var(--brand-red); color: var(--white);
    text-align: right; padding: 5px 11px 0 0;
  }
  .contact__phone { font-size: 14px; font-weight: 500; line-height: 16px; letter-spacing: 0.3px; }
  .contact__line { font-size: 10.8px; line-height: 13px; }

  /* front tagline */
  .tagline {
    position: absolute; left: 43px; top: 487px;
    color: var(--white); font-size: 33px; font-weight: 700; line-height: 34px; letter-spacing: -0.3px;
  }
</style>
</head>
<body>

<section class="leaflet leaflet--back" aria-label="Leaflet reverse side">
  <p class="brand-name">HOLLIVERS</p>

  <div class="accent-bar"></div>
  <div class="gallery">
    <div class="gallery__photo gallery__photo--1" role="img" aria-label="White rendered corner townhouse with hedged front garden"></div>
    <div class="gallery__photo gallery__photo--2" role="img" aria-label="Red brick Victorian terrace with white painted bay fronts"></div>
    <div class="gallery__photo gallery__photo--3" role="img" aria-label="Red brick detached house with gables under a blue sky"></div>
    <div class="gallery__photo gallery__photo--4" role="img" aria-label="Edwardian red brick villa with leafy front garden"></div>
  </div>

  <svg class="office-icon" viewBox="0 0 27 27" fill="none" stroke="#1e1e1e" stroke-width="1.4" aria-hidden="true">
    <rect x="1" y="1" width="13" height="25"/>
    <rect x="14" y="9" width="11" height="17"/>
    <path d="M5 6h4M5 11h4M5 16h4M5 21h4M18 14h3M18 19h3"/>
  </svg>
  <div class="details details--office">
    <p class="details__title">OUR OFFICE</p>
    <p>48 Elm Grove, Hove, BN3 9ZQ</p>
  </div>
  <div class="details details--hours">
    <p class="details__title">OPENING TIMES</p>
    <p>Monday to Friday: 8.45am - 6:30pm</p>
    <p>Saturday: 8.45am - 5pm</p>
    <p>Sunday: By appointment only</p>
    <p>Open 7 days a week</p>
  </div>

  <h1 class="headline">SELL<br>YOUR<br>HOME</h1>
  <p class="offer">from 1st December 2021 until<br>7th January 2022 and receive<br>50% off HOLLIVERS fees</p>

  <div class="story-rule"></div>
  <article class="story">
    <h2 class="story__title">THINKING OF MOVING HOME?</h2>
    <p class="story__body">We have created an estate agency which offers a first class personal service with an honest and friendly approach. Having been open for only a year we have earned a name as one of the fastest growing estate agents in all Brighton &amp; Hove. Hollivers are extremely active in generating sales and achieving record breaking prices on premium properties in Hove. We have several serious buyers who are keen to purchase a property in the Hove area.</p>
  </article>

  <div class="contact-icons" aria-hidden="true">
    <svg viewBox="0 0 16 13"><path d="M3 1l3 3-1.5 1.5c1 2 2.5 3.5 4.5 4.5L10.5 8.5l3 3-1.5 1.5C7 12.5 3.5 9 2 2.5z" fill="#c00000"/></svg>
    <svg viewBox="0 0 16 13" fill="none" stroke="#c00000" stroke-width="1.4"><rect x="1" y="2" width="14" height="9"/><path d="M1 2l7 5 7-5M1 11l5-4.5M15 11l-5-4.5"/></svg>
    <svg viewBox="0 0 16 13" fill="none" stroke="#c00000" stroke-width="1.1"><circle cx="8" cy="6.5" r="5.8"/><ellipse cx="8" cy="6.5" rx="2.6" ry="5.8"/><path d="M2.2 6.5h11.6M3 3.6h10M3 9.4h10"/></svg>
  </div>
  <div class="contact">
    <p class="contact__phone">01273 555 014</p>
    <p class="contact__line">sales@holliversestateagents.co.uk</p>
    <p class="contact__line">www.holliversestateagents.co.uk</p>
  </div>
</section>

<section class="leaflet leaflet--front" aria-label="Leaflet front side">
  <p class="brand-name">HOLLIVERS</p>
  <h2 class="tagline">LET US<br>TREAT YOU<br>THIS CHRISTMAS</h2>
</section>

</body>
</html>
```